Higher co-efficient of performance means more heat for your money

I need a bar graph that will have the following heating systems, 80% efficient gas furnace COP of .8, Electric heat COP of 1, and Our best selling heat pump with a cop of 4 at 47F. I will have a constant bar, 100$ worth of gas for furnace, 100$ of electricity for electric heat, and 100$ worth of electricity for our heat pumps. next to them I will have a bar showing how much heat each heating system will provide for $100 of fuel. For gas furnace I need a bar that says $80 worth of heat and the barograph to match it, for electric heat I need the bar to show 100$ worth of heat, for our best selling heat pump I need the bar graph to show and say $400 dollars worth of heat. Please take a look at my website www.brightmarkcomfort.example for brand color and feel

```html
<!DOCTYPE html>
<html lang="en">
<head>
<meta charset="utf-8">
<title>Brightmark Comfort – Heat for your money</title>
<link rel="stylesheet" href="https://fonts.googleapis.com/css2?family=Open+Sans:wght@400;600&display=swap">
<style>
  :root {
    --brand-blue: #0070bd;
    --brand-red: #c8202f;
    --label-grey: #6b6b6b;
    --paper: #ffffff;
  }
  html, body {
    margin: 0;
    padding: 0;
    width: 1200px;
    height: 1200px;
    overflow: hidden;
    background: var(--paper);
    font-family: "Open Sans", sans-serif;
  }
  .canvas {
    position: relative;
    width: 1200px;
    height: 1200px;
  }
  .frame {
    position: absolute;
    left: 154px;
    top: 234px;
    width: 898px;
    height: 737px;
    box-sizing: border-box;
    border: 20px solid var(--brand-blue);
  }
  .brand {
    position: absolute;
    left: 264px;
    top: 395px;
    display: flex;
    align-items: center;
    gap: 10px;
    color: var(--brand-blue);
    font-weight: 600;
    font-size: 24px;
    letter-spacing: 1px;
  }
  .brand-dot {
    width: 18px;
    height: 18px;
    border-radius: 50%;
    background: var(--brand-red);
  }
  .headline {
    position: absolute;
    left: 263px;
    top: 517px;
    margin: 0;
    color: var(--brand-blue);
    font-size: 18px;
    font-weight: 400;
    line-height: 25px;
  }
  .footnote {
    position: absolute;
    left: 263px;
    top: 577px;
    margin: 0;
    color: var(--brand-blue);
    font-size: 18px;
  }
  .chart {
    position: absolute;
    left: 0;
    top: 0;
  }
  .bar { fill: var(--brand-blue); }
  .axis, .divider { stroke: var(--brand-blue); stroke-width: 1.5; }
  .icon-disc { fill: var(--paper); }
  .icon { fill: var(--brand-blue); }
  .bar-label { fill: var(--paper); font-size: 17px; font-family: "Open Sans", sans-serif; }
  .group-label { fill: var(--label-grey); font-size: 19px; font-family: "Open Sans", sans-serif; }
</style>
</head>
<body>
<div class="canvas">
  <div class="frame"></div>

  <div class="brand"><span class="brand-dot"></span>BRIGHTMARK COMFORT</div>

  <p class="headline">High Co-Efficient of performance<br>means more heat for your money</p>
  <p class="footnote">*Co² measure at 47ºF</p>

  <svg class="chart" width="1200" height="1200" viewBox="0 0 1200 1200" role="img" aria-label="Bar chart: heat delivered for $100 of fuel">
    <!-- axis -->
    <line class="axis" x1="215" y1="886" x2="991" y2="886"/>
    <circle class="icon" cx="215" cy="886" r="2.5"/>
    <circle class="icon" cx="991" cy="886" r="2.5"/>

    <!-- group dividers -->
    <line class="divider" x1="470" y1="639" x2="470" y2="886"/>
    <line class="divider" x1="719" y1="639" x2="719" y2="886"/>

    <!-- gas furnace -->
    <g class="bar-group gas">
      <rect class="bar" x="257" y="694" width="75" height="221" rx="37.5"/>
      <circle class="icon-disc" cx="294.5" cy="880" r="32"/>
      <path class="icon" d="M277 892 a8 8 0 0 1 3 -15 a9 9 0 0 1 16 -4 a7 7 0 0 1 12 6 a7 7 0 0 1 1 13 z"/>
      <text class="bar-label" transform="translate(301 840) rotate(-90)">100 of Co2</text>

      <rect class="bar" x="355" y="736" width="75" height="179" rx="37.5"/>
      <circle class="icon-disc" cx="392.5" cy="880" r="32"/>
      <path class="icon" d="M392 864 c4 7 14 12 14 22 a13 13 0 0 1 -26 0 c0 -6 3 -10 7 -13 c0 4 2 7 4 8 c0 -6 0 -11 1 -17 z"/>
      <text class="bar-label" transform="translate(399 840) rotate(-90)">80 of Heat</text>

      <text class="group-label" transform="translate(457 872) rotate(-90)">80% Gas</text>
    </g>

    <!-- electric heat -->
    <g class="bar-group electric">
      <rect class="bar" x="502" y="694" width="75" height="221" rx="37.5"/>
      <circle class="icon-disc" cx="539.5" cy="880" r="32"/>
      <path class="icon" d="M546 859 l-18 25 h10 l-5 20 l18 -26 h-10 z"/>
      <text class="bar-label" transform="translate(546 845) rotate(-90)">100 of Electric</text>

      <rect class="bar" x="600" y="694" width="75" height="221" rx="37.5"/>
      <circle class="icon-disc" cx="637.5" cy="880" r="32"/>
      <path class="icon" d="M637 864 c4 7 14 12 14 22 a13 13 0 0 1 -26 0 c0 -6 3 -10 7 -13 c0 4 2 7 4 8 c0 -6 0 -11 1 -17 z"/>
      <text class="bar-label" transform="translate(644 845) rotate(-90)">100 of Heat</text>

      <text class="group-label" transform="translate(703 872) rotate(-90)">Electric / Heat</text>
    </g>

    <!-- heat pump -->
    <g class="bar-group heat-pump">
      <rect class="bar" x="757" y="694" width="75" height="221" rx="37.5"/>
      <circle class="icon-disc" cx="794.5" cy="880" r="32"/>
      <path class="icon" d="M801 859 l-18 25 h10 l-5 20 l18 -26 h-10 z"/>
      <text class="bar-label" transform="translate(801 840) rotate(-90)">100 of Electric</text>

      <rect class="bar" x="855" y="277" width="75" height="638" rx="37.5"/>
      <circle class="icon-disc" cx="892.5" cy="880" r="32"/>
      <path class="icon" d="M892 864 c4 7 14 12 14 22 a13 13 0 0 1 -26 0 c0 -6 3 -10 7 -13 c0 4 2 7 4 8 c0 -6 0 -11 1 -17 z"/>
      <text class="bar-label" transform="translate(899 840) rotate(-90)">400 worth of heat</text>

      <text class="group-label" transform="translate(962 872) rotate(-90)">Our Best Selling Heat Pump</text>
    </g>
  </svg>
</div>
</body>
</html>
```